K.T.W Services

We are needing business cards for a construction company that does everything from painting and detailing, maintenance, Sheetrock repairs, demolition, tile and wood floors. Also, K.T.W stands for Detailing, maintenance, and Painting. We would like the colors to be closer to the colors grey and light brown/khaki, but if there is any other suggestions that would go better with the design we are open to ideas.

Industry/Entity Type

Business

Contact Information for Business Card

Owner / Operator Owen Haskell (555) 314-2097 / (555) 482- 3916

Font styles to use
Sans Serif

```html
<!DOCTYPE html>
<html lang="en">
<head>
<meta charset="utf-8">
<title>K.T.W Services – Business Card</title>
<link rel="stylesheet" href="https://fonts.googleapis.com/css2?family=Montserrat:wght@400;500&family=Open+Sans:wght@400&display=swap">
<style>
  :root {
    --backdrop: #e9e7e3;
    --card-light: #ffffff;
    --card-shade: #eeeeec;
    --gold: #c2a372;
    --gold-deep: #a9875a;
    --grey-text: #a3a3a3;
    --divider: #b08d5e;
  }
  * { margin: 0; padding: 0; box-sizing: border-box; }
  html, body {
    width: 1200px;
    height: 780px;
    overflow: hidden;
    background: var(--backdrop);
  }
  .canvas {
    width: 1200px;
    height: 780px;
    display: flex;
    align-items: center;
    justify-content: center;
  }
  .business-card {
    position: relative;
    width: 1050px;
    height: 600px;
    border-radius: 30px;
    background: radial-gradient(ellipse at 55% 40%, var(--card-light) 0%, var(--card-light) 45%, var(--card-shade) 100%);
    box-shadow: 0 6px 18px rgba(0,0,0,0.12);
  }
  .brand {
    position: absolute;
    left: 110px;
    top: 190px;
    color: var(--gold);
    font-family: "Montserrat", sans-serif;
    line-height: 1;
  }
  .brand-initials {
    display: block;
    font-size: 150px;
    font-weight: 500;
    letter-spacing: 2px;
  }
  .brand-word {
    display: block;
    margin-top: 8px;
    font-size: 76px;
    font-weight: 400;
    letter-spacing: 1px;
  }
  .divider {
    position: absolute;
    left: 585px;
    top: 190px;
    width: 2px;
    height: 190px;
    background: linear-gradient(to bottom, rgba(176,141,94,0) 0%, var(--divider) 50%, rgba(176,141,94,0) 100%);
  }
  .contact {
    position: absolute;
    left: 640px;
    top: 150px;
    font-family: "Open Sans", sans-serif;
  }
  .contact-name {
    color: var(--gold-deep);
    font-family: "Montserrat", sans-serif;
    font-weight: 500;
    font-size: 36px;
    letter-spacing: 1px;
    text-transform: uppercase;
  }
  .contact-role {
    color: var(--grey-text);
    font-size: 24px;
    margin-top: 4px;
  }
  .phone-list {
    list-style: none;
    margin-top: 34px;
  }
  .phone-item {
    display: flex;
    align-items: center;
    gap: 12px;
    color: var(--grey-text);
    font-size: 26px;
    margin-bottom: 8px;
  }
  .phone-icon {
    width: 30px;
    height: 30px;
    flex: none;
  }
</style>
</head>
<body>
<main class="canvas">
  <section class="business-card" aria-label="K.T.W Services business card">
    <div class="brand">
      <span class="brand-initials">K.T.W</span>
      <span class="brand-word">SERVICES</span>
    </div>

    <div class="divider"></div>

    <div class="contact">
      <h1 class="contact-name">Owen Haskell</h1>
      <p class="contact-role">Owner / Operator</p>
      <ul class="phone-list">
        <li class="phone-item">
          <svg class="phone-icon" viewBox="0 0 30 30" aria-hidden="true">
            <rect width="30" height="30" rx="5" fill="var(--gold)"/>
            <path d="M10 8c1-1 2-1 3 0l1.5 2.5c.5 1 .2 1.8-.6 2.4l-.9.7c.8 1.8 2.2 3.2 4 4l.7-.9c.6-.8 1.4-1.1 2.4-.6L22.5 17c1 1 1 2 0 3l-1 1c-1.5 1.5-5 .5-8.3-2.8S7.5 10.5 9 9z" fill="#fff"/>
          </svg>
          <span>(555) 314-2097</span>
        </li>
        <li class="phone-item">
          <svg class="phone-icon" viewBox="0 0 30 30" aria-hidden="true">
            <rect width="30" height="30" rx="5" fill="var(--gold)"/>
            <path d="M10 8c1-1 2-1 3 0l1.5 2.5c.5 1 .2 1.8-.6 2.4l-.9.7c.8 1.8 2.2 3.2 4 4l.7-.9c.6-.8 1.4-1.1 2.4-.6L22.5 17c1 1 1 2 0 3l-1 1c-1.5 1.5-5 .5-8.3-2.8S7.5 10.5 9 9z" fill="#fff"/>
          </svg>
          <span>(555) 482- 3916</span>
        </li>
      </ul>
    </div>
  </section>
</main>
</body>
</html>
```